Tavisco hd highway sign

would like a comercial truck in backround, and would like it very easy to read. Must have company name Tavisco H.D. Mechanical
would like address included 5912 quillby frontage road. would a some bullet points on sign
-Commercial truck and trailer inspection and repair
-Heavy equipment repair
-24/7 Mobile service

```html
<!DOCTYPE html>
<html lang="en">
<head>
<meta charset="utf-8">
<title>Tavisco H.D. Mechanical – Highway Sign</title>
<link href="https://fonts.googleapis.com/css2?family=Poppins:wght@600;700;800&display=swap" rel="stylesheet">
<style>
  :root {
    --night: #05080c;
    --deep-navy: #0d1a24;
    --fog: #1d3342;
    --glow-cyan: #5fd0ff;
    --glow-soft: #9fe6ff;
    --pill-start: #45c2f2;
    --pill-end: #a6ecff;
    --ink-navy: #0b2233;
    --white: #ffffff;
  }
  html, body {
    margin: 0;
    padding: 0;
    width: 1200px;
    height: 358px;
    overflow: hidden;
    background: var(--night);
  }
  .sign {
    position: relative;
    width: 1200px;
    height: 358px;
    overflow: hidden;
    font-family: "Poppins", sans-serif;
    background:
      radial-gradient(ellipse 520px 160px at 900px 250px, rgba(90,140,170,0.35), transparent 70%),
      linear-gradient(180deg, var(--night) 0%, #08121a 45%, var(--deep-navy) 70%, #14222c 100%);
  }
  .truck-photo {
    position: absolute;
    left: 600px;
    top: 18px;
    width: 562px;
    height: 318px;
    border-radius: 40px 60px 20px 20px;
    background:
      radial-gradient(ellipse 260px 150px at 40% 55%, rgba(95,208,255,0.35), transparent 70%),
      linear-gradient(160deg, #16242f 0%, #0c151c 60%, #1a2a35 100%);
  }
  .company-name {
    position: absolute;
    left: 31px;
    top: 34px;
    margin: 0;
    font-weight: 800;
    font-size: 82px;
    line-height: 72px;
    letter-spacing: -0.5px;
    color: var(--glow-cyan);
    text-shadow: 0 0 14px rgba(95,208,255,0.75), 0 0 30px rgba(95,208,255,0.45);
  }
  .address-pill {
    position: absolute;
    left: 33px;
    top: 203px;
    width: 458px;
    height: 43px;
    border-radius: 22px;
    background: linear-gradient(90deg, var(--pill-start), var(--pill-end));
    box-shadow: 0 0 16px rgba(95,208,255,0.5);
    display: flex;
    align-items: center;
  }
  .address-pill svg {
    margin-left: 6px;
    width: 34px;
    height: 34px;
  }
  .address-text {
    margin-left: 8px;
    font-weight: 600;
    font-size: 30px;
    color: var(--ink-navy);
    line-height: 1;
  }
  .services {
    position: absolute;
    left: 36px;
    top: 262px;
    margin: 0;
    padding: 0;
    list-style: none;
  }
  .services li {
    position: relative;
    padding-left: 20px;
    font-weight: 600;
    font-size: 16px;
    line-height: 26px;
    color: var(--white);
  }
  .services li::before {
    content: "";
    position: absolute;
    left: 0;
    top: 10px;
    width: 7px;
    height: 7px;
    border-radius: 50%;
    background: var(--glow-soft);
  }
</style>
</head>
<body>
  <main class="sign">
    <div class="truck-photo" role="img" aria-label="Commercial semi truck cab with glowing cyan light lines, parked in misty night setting"></div>

    <h1 class="company-name">TAVISCO H.D.<br>MECHANICAL</h1>

    <div class="address-pill">
      <svg viewBox="0 0 34 34" aria-hidden="true">
        <circle cx="17" cy="17" r="15" fill="none" stroke="var(--ink-navy)" stroke-width="2.4"/>
        <path d="M17 8.5a6 6 0 0 0-6 6c0 4.5 6 11 6 11s6-6.5 6-11a6 6 0 0 0-6-6z" fill="var(--ink-navy)"/>
        <circle cx="17" cy="14.5" r="2.2" fill="var(--pill-start)"/>
      </svg>
      <span class="address-text">5912 quillby frontage road</span>
    </div>

    <ul class="services">
      <li>Commercial truck and trailer inspection and repair</li>
      <li>Heavy equipment repair</li>
      <li>24/7 Mobile service</li>
    </ul>
  </main>
</body>
</html>
```